Quorvin Upcoming Gigs

One page graphic with my upcoming dates. Logo and photo attached, and sample from last flyer. Text:

QUORVIN

UPCOMING DATES

3/26/18 Tidal Plums (Las Vegas, NV)

4/1/18 Venture Hollow 2847 M St (Sac, CA)

4/8/18 Amber Heron (Sac, CA)

5/5/18 Low Ceiling @ Silver Moth (Sac, CA)

5/10/18 Pellman Art Museum (Sac, CA)

5/11/18 Vif Brume @ Cafe du Lierre (Sac, CA)

5/27/18 Sonnlicht JTR @ Vox (Sac, CA)

Save The Date: 9/21/18 Lanterns Festival (Puerto Nuevo, MX)

plazabook.example/quorvin482

Target Market(s)

House/Electronic Music

Industry/Entity Type

Night Club

Font styles to use
Sans Serif

Colors

Designer to choose colors to be used in the design.

Requirements
Must have
• Quorvin logo or something that looks good instead. Prefer photo to be in but not necessary.
Nice to have

```html
<!DOCTYPE html>
<html lang="en">
<head>
<meta charset="utf-8">
<title>Quorvin – Upcoming Dates</title>
<link rel="stylesheet" href="https://fonts.googleapis.com/css2?family=Montserrat:wght@800&family=Oswald:wght@300;500;600&display=swap">
<style>
  :root {
    --page: #ffffff;
    --ink: #000000;
    --blue: #0a36b0;
    --blue-bright: #0b3ec9;
    --navy-1: #0a2a90;
    --navy-2: #0a1a52;
    --navy-3: #041036;
    --gold: #f5a623;
    --white: #ffffff;
  }
  html, body {
    margin: 0;
    width: 1200px;
    height: 745px;
    overflow: hidden;
    background: var(--page);
  }
  .banner {
    position: absolute;
    left: 0;
    top: 90px;
    width: 1200px;
    height: 566px;
    background: var(--ink);
    overflow: hidden;
  }
  .banner-art {
    position: absolute;
    inset: 0;
  }
  .headline {
    position: absolute;
    left: 38px;
    top: 52px;
    margin: 0;
    font-family: "Montserrat", sans-serif;
    font-weight: 800;
    font-size: 84px;
    line-height: 1;
    color: var(--blue-bright);
    letter-spacing: 0;
  }
  .subhead {
    position: absolute;
    left: 42px;
    top: 150px;
    margin: 0;
    font-family: "Montserrat", sans-serif;
    font-weight: 800;
    font-size: 45px;
    line-height: 1;
    color: var(--white);
    letter-spacing: 1px;
  }
  .gig-list {
    position: absolute;
    left: 42px;
    top: 208px;
    margin: 0;
    padding: 0;
    list-style: none;
    font-family: "Oswald", sans-serif;
    font-size: 23px;
    line-height: 33.2px;
    color: var(--white);
    letter-spacing: -0.2px;
  }
  .gig-date {
    display: inline-block;
    width: 87px;
    color: var(--gold);
    font-weight: 500;
  }
  .gig-venue { font-weight: 300; }
  .gig-place { font-weight: 600; }
  .save-date {
    position: absolute;
    left: 42px;
    top: 455px;
    font-family: "Oswald", sans-serif;
    color: var(--gold);
    font-size: 23px;
    line-height: 30px;
  }
  .save-date strong { font-weight: 500; display: block; }
  .save-date span { font-weight: 300; display: block; }
  .social {
    position: absolute;
    left: 908px;
    top: 467px;
    display: flex;
    align-items: center;
    gap: 12px;
    font-family: "Oswald", sans-serif;
    font-weight: 500;
    font-size: 23px;
    line-height: 30px;
    color: var(--white);
  }
  .social-mark {
    width: 22px;
    height: 22px;
    background: var(--white);
    border-radius: 3px;
  }
</style>
</head>
<body>
  <section class="banner">
    <svg class="banner-art" width="1200" height="566" viewBox="0 0 1200 566">
      <defs>
        <linearGradient id="stage-light" x1="0" y1="0" x2="1" y2="1">
          <stop offset="0" stop-color="#3a2fa8"/>
          <stop offset="0.45" stop-color="#8a3a7a"/>
          <stop offset="0.75" stop-color="#c4564a"/>
          <stop offset="1" stop-color="#2a1430"/>
        </linearGradient>
        <linearGradient id="pattern-tone" x1="0" y1="0" x2="0" y2="1">
          <stop offset="0" stop-color="#0a2a90"/>
          <stop offset="1" stop-color="#061448"/>
        </linearGradient>
        <linearGradient id="corner-tone" x1="0" y1="0" x2="1" y2="1">
          <stop offset="0" stop-color="#041036"/>
          <stop offset="1" stop-color="#0a2a90"/>
        </linearGradient>
      </defs>
      <polygon class="accent-stripe" points="480,0 534,0 664,261 637,315" fill="var(--navy-2)"/>
      <polygon class="accent-wedge" points="534,0 858,0 664,261" fill="var(--blue)"/>
      <polygon class="pattern-area" role="img" aria-label="Decorative pattern of navy and blue triangles"
               points="611,188 664,261 880,566 470,566 400,488" fill="url(#pattern-tone)"/>
      <polygon class="photo-area" role="img" aria-label="Photo of the DJ performing at the decks under purple and red stage light"
               points="858,0 1200,0 1200,566 880,566 664,261" fill="url(#stage-light)"/>
      <polygon class="pattern-corner" role="img" aria-label="Decorative pattern of navy and blue triangles"
               points="1060,0 1200,0 1200,300" fill="url(#corner-tone)"/>
      <polygon class="band band-left" points="0,450 428,450 382,519 0,519" fill="var(--blue)"/>
      <polygon class="band band-right" points="843,450 1200,450 1200,519 800,519" fill="var(--blue)"/>
    </svg>

    <h1 class="headline">QUORVIN</h1>
    <h2 class="subhead">UPCOMING DATES</h2>

    <ul class="gig-list">
      <li><span class="gig-date">3/26/18</span><span class="gig-venue">Tidal Plums </span><span class="gig-place">(Las Vegas, NV)</span></li>
      <li><span class="gig-date">4/1/18</span><span class="gig-venue">Venture Hollow 2847 M St </span><span class="gig-place">(Sac, CA)</span></li>
      <li><span class="gig-date">4/8/18</span><span class="gig-venue">Amber Heron </span><span class="gig-place">(Sac, CA)</span></li>
      <li><span class="gig-date">5/5/18</span><span class="gig-venue">Low Ceiling @ Silver Moth </span><span class="gig-place">(Sac, CA)</span></li>
      <li><span class="gig-date">5/10/18</span><span class="gig-venue">Pellman Art Museum </span><span class="gig-place">(Sac, CA)</span></li>
      <li><span class="gig-date">5/11/18</span><span class="gig-venue">Vif Brume @ Cafe du Lierre </span><span class="gig-place">(Sac, CA)</span></li>
      <li><span class="gig-date">5/27/18</span><span class="gig-venue">Sonnlicht JTR @ Vox </span><span class="gig-place">(Sac, CA)</span></li>
    </ul>

    <div class="save-date">
      <strong>Save The Date: 9/21/18</strong>
      <span>Lanterns Festival (Puerto Nuevo, MX)</span>
    </div>

    <div class="social">
      <span class="social-mark"></span>
      <span class="social-handle">quorvin482</span>
    </div>
  </section>
</body>
</html>
```